Leadership training for women Business + Spirit

I need a flyer for a leadership training to hand out after I've been doing public speaking. I would also like to send it as a PDF. so maybe A4 is a good size. I will probably also need a brochure, with some more in depth information, but to start with I like to just give them something so they get inspired to contact me for more information. You can see more of my style on www.brightlantern.se . Its a training that combines business with spirit, heart with intellect. We focus both on strict leadership skills such as Setting objectives aligned with strategy, assess performance and spiritual practices such as meditation, connecting with your unique essence. I like the deign to communicate business and professional together with warmth, life and joy. Colourful with style. Empowerment. The attached style guide does not have to be followed strictly but please use it in combination with my site www.brightlantern.se I've the logo in many different sizes. I've added the smallest one below. Use any images that you think might fit, doesn't have to be from my website, it could be from your resources. I've added some other images here in the brief too, I have many more but can't attach all of it :-).
Women in leadership positions age 30 - 60
Leadership

```html
<!DOCTYPE html>
<html lang="en">
<head>
<meta charset="utf-8">
<title>Bright Lantern – Leadership flyer</title>
<link href="https://fonts.googleapis.com/css2?family=Lato:wght@400;700;900&display=swap" rel="stylesheet">
<style>
  :root {
    --orange: #f5a021;
    --orange-deep: #ef8a1c;
    --navy: #13344f;
    --navy-text: #17375a;
    --grey-line: #8f97a3;
    --magenta: #c42589;
    --magenta-deep: #8f1f6e;
    --white: #ffffff;
  }
  * { box-sizing: border-box; margin: 0; padding: 0; }
  html, body { width: 950px; height: 1200px; overflow: hidden; background: #d4d5d7; }
  body { font-family: "Lato", sans-serif; }
  .flyer { position: relative; width: 950px; height: 1200px; overflow: hidden; background: var(--navy); }

  /* Intro band */
  .intro { position: absolute; left: 0; top: 0; width: 950px; height: 400px;
    background: radial-gradient(ellipse at 70% 30%, #f9b13a 0%, var(--orange) 45%, var(--orange-deep) 100%); }
  .intro-wave { position: absolute; left: 0; top: 320px; width: 950px; height: 80px; }
  .portrait { position: absolute; left: 62px; top: 51px; width: 222px; height: 262px;
    border: 4px solid var(--white); border-radius: 22px;
    background: linear-gradient(160deg, #6e4a3e 0%, #3b2f2c 45%, #1f2630 100%); }
  .coach-name { position: absolute; left: 310px; top: 52px; width: 610px; text-align: center;
    color: var(--navy-text); font-weight: 900; font-size: 29px; line-height: 36px; }
  .coach-bio { position: absolute; left: 314px; top: 97px; width: 572px; text-align: center;
    color: var(--navy-text); font-size: 14.4px; line-height: 18.2px; }
  .coach-bio p + p { margin-top: 18.2px; }
  .coach-quote { position: absolute; left: 310px; top: 284px; width: 610px; text-align: center;
    color: var(--navy-text); font-weight: 700; font-size: 19.5px; line-height: 24px; }

  /* Brand block */
  .brand-ring { position: absolute; left: 155px; top: 388px; width: 144px; height: 144px;
    border-radius: 50%; border: 3px solid var(--white); }
  .brand-name { position: absolute; left: 318px; top: 420px; color: var(--white);
    font-weight: 400; font-size: 80px; line-height: 80px; letter-spacing: -1px; white-space: nowrap; }
  .mission { position: absolute; left: 31px; top: 548px; width: 887px; height: 106px;
    border: 3px solid var(--white); }
  .mission-title { position: absolute; left: 50%; top: -19px; transform: translateX(-50%);
    background: var(--navy); padding: 0 14px; color: var(--white); font-weight: 700;
    font-size: 30px; line-height: 34px; white-space: nowrap; }
  .mission-text { padding: 15px 24px 0; text-align: center; color: var(--white);
    font-size: 14.6px; line-height: 18.2px; }

  /* Pillars */
  .pillars { position: absolute; left: 0; top: 679px; width: 950px; height: 441px;
    background: linear-gradient(180deg, var(--magenta-deep) 0%, var(--magenta) 45%, #b42282 75%, var(--magenta-deep) 100%); }
  .pillar { position: absolute; top: 29px; width: 254px; }
  .pillar-photo { width: 254px; height: 156px; border: 4px solid var(--white);
    box-shadow: 4px 4px 0 rgba(255,255,255,0.85); }
  .pillar-text { margin: 32px auto 0; width: 236px; text-align: center; color: var(--white);
    font-size: 13.3px; line-height: 16.4px; }
  .pillar--one { left: 45px; }
  .pillar--two { left: 346px; }
  .pillar--three { left: 647px; }
  .pillar--three .pillar-text { width: 226px; }
  .photo-shore { background: linear-gradient(180deg, #dfe4ea 0%, #b9c3cc 45%, #c9b9a1 70%, #a99275 100%); }
  .photo-blossom { background: radial-gradient(circle at 55% 55%, #e58bb3 0%, #a8486e 40%, #3e1d22 100%); }
  .photo-dunes { background: linear-gradient(180deg, #c99865 0%, #b27a48 55%, #d3a674 100%); }

  /* Footer */
  .contact { position: absolute; left: 0; top: 1120px; width: 950px; height: 80px;
    background: var(--navy); display: flex; align-items: center; justify-content: center;
    color: var(--white); font-weight: 900; font-size: 26px; }
</style>
</head>
<body>
<main class="flyer">
  <section class="intro">
    <div class="portrait" role="img" aria-label="Portrait photo of the coach in a dark blazer and cream turtleneck against a brick wall"></div>
    <h1 class="coach-name">Maja Lindqvist Hale</h1>
    <div class="coach-bio">
      <p>I am a modern mystic and leadership developer who has trained several hundreds of leaders on eg. Norrbank, Dalmjölk, Ravnbryg, Stegsko, Skydda Försäkring, Vindkraft Nord, Netbolag. I have been on my spiritual journey since childhood, meditated since I was 16 and after a decade of extreme skiing and rock climbing I have weighted my adult professional life on the spiritual awakening and to coach people to a more living life.</p>
      <p>With BRIGHT LANTERN I offer opportunities for you as a woman to strengthen contact with your inner being and your own very holy wisdom. To unite the interior with the exterior and deepen your leadership, both as a private person and in your professional role. You are very welcome!</p>
    </div>
    <p class="coach-quote">"I live as I learn, that's my strength."</p>
    <svg class="intro-wave" viewBox="0 0 950 80" preserveAspectRatio="none" aria-hidden="true">
      <path d="M420 72 C 600 66, 780 50, 950 8" fill="none" stroke="var(--grey-line)" stroke-width="7"/>
      <path d="M0 80 L0 76 C 200 56, 340 70, 500 76 C 700 78, 840 52, 950 18 L950 80 Z" fill="var(--navy)"/>
    </svg>
  </section>

  <span class="brand-ring" aria-hidden="true"></span>
  <p class="brand-name">Bright Lantern</p>

  <section class="mission">
    <h2 class="mission-title">BRIGHT LANTERN</h2>
    <p class="mission-text">We have become good at performing at the expense of contact with our body and soul, when we really need the opposite. A holistic leadership of people who have good self-knowledge, who grow in the challenges, people who know that vulnerability gives an incomparable strength and does not underestimate their brilliant intellect. The world needs people who live and lead from a whole new place. The show feminine can lead us there.</p>
  </section>

  <section class="pillars">
    <article class="pillar pillar--one">
      <div class="pillar-photo photo-shore" role="img" aria-label="Photo of a thoughtful woman standing on a beach by the sea"></div>
      <p class="pillar-text">As modern women, many of us share a basic pattern of just pushing through and biting, delivering and being good by driving over both body and soul. What if there is another way to get results? A way in which you combine practical skills in leadership such as goals, performance management and coaching with presence in both body, heart and soul. A way that lets soul, heart, achievement and business go hand in hand.</p>
    </article>
    <article class="pillar pillar--two">
      <div class="pillar-photo photo-blossom" role="img" aria-label="Photo of pink cherry blossoms on a branch"></div>
      <p class="pillar-text">Before spirituality became its own concept and concept, before the word even emerged or religions and new age seized it, it already existed as a natural part of our lives. We are all valuable just by being, without performing. We are all in contact with something bigger, everything is connected and is part of the same being. Life is sacred. Remembering and living this is spirituality for me.</p>
    </article>
    <article class="pillar pillar--three">
      <div class="pillar-photo photo-dunes" role="img" aria-label="Photo of a woman with raised arms in golden sand dunes"></div>
      <p class="pillar-text">We live in a culture that teaches us to shut down, keep the cover on our dreams and constantly put what is most important to us at the bottom of the list, while we are rushing towards a future that promises us all that we do not take time till now. Bright Lantern is a context that strengthens you, both as being and woman to wake up, grow and succeed with what you want to live before you die. It's empowerment!</p>
    </article>
  </section>

  <footer class="contact">0739-55 18 27 | BRIGHTLANTERN.SE | Folj oss pa: circlebook</footer>
</main>
</body>
</html>
```